Report Cover Page for bioenergy

We need a cover page design that is simple, elegant, and modern. We see designs in whites, blues and greys. The cover page should be very close to the one in the first attachment in terms of layout (ie big logo with pictures in it-- but not so 90s. Maybe more sleek, fine, modern, elegant. Look to the second page for an example of the font, and colors and style of the report. They should go together.

These reports are sold for about $30,000 each and companies will make decisions on whether or not to invest

Target Market(s)

Project developers and investment bankers.

Font styles to use
Sans Serif

Colors
33a6d7
0592cd
85cae6
cee9f5
0355a3
3276b5
85abd2
eaf1f7
ffffff

Requirements
Must have
• match the report attached in terms of style and font and colors
• have a strong logo like the attached file.
• should convey professionalism and insight and trustworthiness
• should make the reader eager to turn the page and start reading the report.
• Modern refined professional
Should not have
• greens

```html
<!DOCTYPE html>
<html lang="en">
<head>
<meta charset="utf-8">
<title>Pellet Mill Feedstock Supply Assessment – Cover</title>
<link rel="stylesheet" href="https://fonts.googleapis.com/css2?family=Dosis:wght@500&family=Roboto:wght@400&display=swap">
<style>
  :root {
    --canvas: #d4d6d8;
    --page-top: #ffffff;
    --page-bottom: #ececec;
    --ink: #1c1c1c;
    --label: #6b6b6b;
    --brand-grey: #6e6e6e;
    --accent: #0592cd;
    --accent-bright: #33a6d7;
    --tagline: #3276b5;
    --white: #ffffff;
  }
  * { margin: 0; padding: 0; box-sizing: border-box; }
  html, body { width: 1200px; height: 861px; overflow: hidden; }
  body { background: var(--canvas); position: relative; }

  .cover {
    position: absolute;
    left: 300px; top: 38px;
    width: 600px; height: 784px;
    background: linear-gradient(160deg, var(--page-top) 0%, #f6f6f6 55%, var(--page-bottom) 100%);
    overflow: hidden;
  }
  .cover-art { position: absolute; inset: 0; width: 100%; height: 100%; }

  .cover-title {
    position: absolute;
    left: 61px; top: 84px;
    font-family: "Dosis", sans-serif;
    font-weight: 500;
    font-size: 28px;
    line-height: 35px;
    color: var(--ink);
  }

  .credit {
    position: absolute;
    right: 38px;
    display: flex; align-items: center; gap: 5px;
    font-family: "Dosis", sans-serif;
    font-weight: 500;
  }
  .credit-label { font-size: 11px; letter-spacing: .3px; color: var(--label); text-transform: uppercase; }
  .credit-name { font-size: 11px; color: var(--white); background: var(--accent-bright); padding: 2px 4px; }
  .credit--client { top: 572px; }
  .credit--author { top: 608px; }

  .brand {
    position: absolute;
    right: 36px; top: 664px;
    display: flex; align-items: center; gap: 12px;
  }
  .brand-dot { width: 40px; height: 40px; border-radius: 50%; background: var(--accent); }
  .brand-name {
    font-family: "Roboto", sans-serif;
    font-weight: 400;
    font-size: 31px;
    line-height: 36px;
    padding-top: 10px;
    color: var(--brand-grey);
    letter-spacing: .5px;
  }
  .brand-tagline {
    position: absolute;
    right: 36px; top: 712px;
    text-align: right;
    font-family: "Roboto", sans-serif;
    font-size: 13px;
    line-height: 19px;
    color: var(--tagline);
    letter-spacing: .3px;
  }
</style>
</head>
<body>
  <main class="cover">
    <svg class="cover-art" viewBox="0 0 492 643" preserveAspectRatio="none">
      <defs>
        <linearGradient id="forest-tone" x1="0" y1="0" x2="1" y2="1">
          <stop offset="0" stop-color="#8fbfe0"/>
          <stop offset=".55" stop-color="#6f8f86"/>
          <stop offset="1" stop-color="#7a6a55"/>
        </linearGradient>
        <linearGradient id="harvest-tone" x1="0" y1="0" x2="1" y2="1">
          <stop offset="0" stop-color="#9cc3e6"/>
          <stop offset=".5" stop-color="#c9a15a"/>
          <stop offset="1" stop-color="#d9c9a6"/>
        </linearGradient>
        <linearGradient id="field-tone" x1="0" y1="0" x2="0" y2="1">
          <stop offset="0" stop-color="#b9cfe0"/>
          <stop offset=".4" stop-color="#9a8f86"/>
          <stop offset="1" stop-color="#7f9a72"/>
        </linearGradient>
      </defs>
      <path class="photo photo--forest" role="img" aria-label="Photo looking up into a canopy of tall pine trees against a blue sky"
            fill="url(#forest-tone)"
            d="M0 352 Q40 310 92 296 Q104 293 112 300 L232 368 Q242 376 234 388 L10 643 L0 643 Z"/>
      <path class="photo photo--harvest" role="img" aria-label="Photo of a machine conveying chipped biomass into a truck"
            fill="url(#harvest-tone)"
            d="M125 288 Q118 280 128 273 Q200 228 272 212 Q282 210 288 215 L374 262 Q380 268 372 276 L262 366 Q254 372 246 367 Z"/>
      <path class="accent-band" fill="#0592cd"
            d="M287 207 Q390 172 492 165 L492 188 Q430 205 388 240 Q380 246 372 240 Z"/>
      <path class="photo photo--field" role="img" aria-label="Photo of an energy crop field in front of a farm building"
            fill="url(#field-tone)"
            d="M383 255 Q430 210 492 188 L492 332 Q430 290 383 262 Z"/>
    </svg>

    <h1 class="cover-title">Pellet Mill Feedstock Supply<br>Assessment</h1>

    <p class="credit credit--client"><span class="credit-label">For</span><span class="credit-name">Harunami Trading</span></p>
    <p class="credit credit--author"><span class="credit-label">Submitted by</span><span class="credit-name">Veltmark Inc.</span></p>

    <div class="brand">
      <span class="brand-dot"></span>
      <span class="brand-name">VELTMARK</span>
    </div>
    <p class="brand-tagline">Careful Analysis<br>Field Insight</p>
  </main>
</body>
</html>
```